KVO mobile detailing

Im starting a mobile detailing company where I go to the clients looking for something that will get good attention and looks professional but also resemble what we do.

It Company

```html
<!DOCTYPE html>
<html lang="en">
<head>
<meta charset="utf-8">
<title>KVO Mobile Detailing – Business Card</title>
<link href="https://fonts.googleapis.com/css2?family=Tinos:wght@400&family=Michroma&display=swap" rel="stylesheet">
<style>
  :root {
    --stage: #000000;
    --card-white: #ffffff;
    --card-shade: #e9ebee;
    --ink: #111111;
    --accent-blue: #1a7fd0;
    --divider-blue: #2a86d6;
    --navy-deep: #0a2556;
    --navy-mid: #0f4d96;
    --navy-light: #1f7ccc;
    --logo-dark: #1b2b3c;
    --logo-light: #ffffff;
  }
  * { box-sizing: border-box; margin: 0; padding: 0; }
  html, body {
    width: 1200px;
    height: 499px;
    overflow: hidden;
    background: var(--stage);
  }
  .canvas {
    position: relative;
    width: 1200px;
    height: 499px;
  }
  .card {
    position: absolute;
    top: 24px;
    width: 573px;
    height: 348px;
    border-radius: 27px;
    overflow: hidden;
  }
  .card-front {
    left: 18px;
    background: linear-gradient(180deg, var(--card-white) 55%, var(--card-shade) 100%);
  }
  .card-back {
    left: 611px;
    background: radial-gradient(ellipse at 70% 35%, var(--navy-light) 0%, var(--navy-mid) 45%, var(--navy-deep) 100%);
  }
  .brand-name {
    position: absolute;
    font-family: "Michroma", sans-serif;
    font-weight: 400;
    text-transform: uppercase;
    white-space: nowrap;
  }
  .brand-line { display: block; }
  .card-front .brand-name {
    left: 30px;
    top: 166px;
    width: 270px;
    font-size: 20px;
    line-height: 1.3;
    letter-spacing: 1px;
    color: var(--logo-dark);
  }
  .card-back .brand-name {
    left: 0;
    right: 0;
    top: 136px;
    text-align: center;
    font-size: 28px;
    line-height: 1.3;
    letter-spacing: 2px;
    color: var(--logo-light);
  }
  .divider {
    position: absolute;
    left: 324px;
    top: 39px;
    width: 3px;
    height: 278px;
    background: var(--divider-blue);
  }
  .details {
    position: absolute;
    left: 348px;
    top: 50px;
    font-family: "Tinos", serif;
  }
  .person-name {
    font-size: 22px;
    color: var(--ink);
    line-height: 1.1;
  }
  .person-role {
    font-size: 15px;
    color: var(--accent-blue);
  }
  .contact {
    margin-top: 32px;
    font-size: 15px;
    color: var(--ink);
  }
  .contact-label { color: var(--accent-blue); margin-right: 6px; }
  .services-title {
    margin-top: 48px;
    font-size: 15px;
    color: var(--ink);
  }
  .services-list {
    list-style: none;
    margin-top: 7px;
  }
  .services-list li {
    font-size: 15px;
    color: var(--accent-blue);
    line-height: 27px;
    position: relative;
    padding-left: 12px;
  }
  .services-list li::before {
    content: "";
    position: absolute;
    left: -4px;
    top: 12px;
    width: 5px;
    height: 5px;
    border-radius: 50%;
    background: var(--ink);
  }
</style>
</head>
<body>
  <main class="canvas">
    <section class="card card-front" aria-label="Business card front">
      <p class="brand-name"><span class="brand-line">KVO mobile</span><span class="brand-line">detailing</span></p>
      <div class="divider"></div>
      <div class="details">
        <p class="person-name">Daniel Moreno</p>
        <p class="person-role">Owner-Operator</p>
        <p class="contact"><span class="contact-label">Contact:</span>555-218-4730</p>
        <p class="services-title">SERVICES</p>
        <ul class="services-list">
          <li>Clay Bar Service</li>
          <li>Exterior Washing</li>
          <li>Paint Sealant</li>
          <li>Waxing</li>
        </ul>
      </div>
    </section>
    <section class="card card-back" aria-label="Business card back">
      <p class="brand-name"><span class="brand-line">KVO mobile</span><span class="brand-line">detailing</span></p>
    </section>
  </main>
</body>
</html>
```